Stationery Design needed for logo design project

This project is linked to Logo: brand identity for modern furniture design studio..

Our company needs a Stationery Design. Please refer to our original project in the link above.

```html
<!DOCTYPE html>
<html lang="en">
<head>
<meta charset="utf-8">
<title>kavna — stationery</title>
<link rel="stylesheet" href="https://fonts.googleapis.com/css2?family=Josefin+Sans:wght@300;400&display=swap">
<style>
  :root {
    --paper: #ffffff;
    --ink: #000000;
    --frame: #333333;
    --text-soft: #444444;
  }
  * { margin: 0; padding: 0; box-sizing: border-box; }
  html, body {
    width: 1178px;
    height: 1200px;
    overflow: hidden;
    background: var(--paper);
    font-family: "Josefin Sans", sans-serif;
    color: var(--ink);
  }
  .canvas { position: relative; width: 1178px; height: 1200px; }

  .letterhead {
    position: absolute;
    left: 24px; top: 22px;
    width: 742px; height: 1148px;
    border: 2px solid var(--frame);
    background: var(--paper);
  }
  .wordmark {
    position: absolute;
    font-family: "Josefin Sans", sans-serif;
    font-weight: 300;
    color: var(--ink);
    line-height: 1;
  }
  .letterhead .wordmark { left: 18px; top: 28px; font-size: 84px; letter-spacing: 1px; }

  .address-line {
    position: absolute;
    left: 0; right: 0;
    text-align: center;
    font-weight: 300;
    color: var(--text-soft);
    white-space: nowrap;
  }
  .letterhead .address-line { bottom: 24px; font-size: 21px; }
  .address-line .sep { margin: 0 1.4em; }
  .address-line .phone-number { font-size: 0.72em; letter-spacing: 1px; }

  .business-card {
    position: absolute;
    left: 815px; top: 118px;
    width: 306px; height: 201px;
    border: 1.5px solid var(--frame);
    background: var(--paper);
  }
  .business-card .wordmark { left: 10px; top: 14px; font-size: 34px; }
  .card-holder {
    position: absolute;
    left: 48px; top: 92px;
    font-weight: 300;
    font-size: 19px;
    letter-spacing: 4px;
    color: var(--text-soft);
  }
  .card-role {
    position: absolute;
    left: 156px; top: 116px;
    font-weight: 300;
    font-size: 9px;
    letter-spacing: 1px;
    color: var(--text-soft);
  }
  .business-card .address-line { bottom: 10px; font-size: 8px; }
  .business-card .address-line .sep { margin: 0 1em; }
</style>
</head>
<body>
<main class="canvas">
  <section class="letterhead" aria-label="Letterhead">
    <div class="wordmark">kavna</div>
    <p class="address-line">14 Lindvej<span class="sep">-</span>Lyon<span class="sep">-</span>telephone <span class="phone-number">1.800.555.0174</span></p>
  </section>

  <section class="business-card" aria-label="Business card">
    <div class="wordmark">kavna</div>
    <p class="card-holder">Emil Varde</p>
    <p class="card-role">designer</p>
    <p class="address-line">14 Lindvej<span class="sep">-</span>Lyon<span class="sep">-</span>telephone <span class="phone-number">1.800.555.0174</span></p>
  </section>
</main>
</body>
</html>
```